Goodnight sleep Collagen milk drink

We need a modern attractive package design for carton . with sachet inside . This is a collagen milk powder targeting young women . 16 - 40 . it contains marine collagen , skim milk powder and other ingredients designed for maintain healthy skin while sleeping. To drink before sleep. the size is 18 cm h x 8.5 cm w x 6.2 cm D , with a slot can tear off on bottom so the sachet can take out .
Updates

Target Market(s)

women , 16 - 40 ,

Industry/Entity Type

Health Care

Colors
0492cd
3176b5
eea4c8
0255a3
6b449b
a54499

Requirements
Must have
• product name : VelvaDorm , clean modern for young women
Nice to have
• represent the idea of beauty , goodnight sleep , elements for ingredients marine collagen , lemon balm , passion flower .

```html
<!DOCTYPE html>
<html lang="en">
<head>
<meta charset="utf-8">
<title>VelvaDorm Collagen Milk Powder – Packaging</title>
<link rel="stylesheet" href="https://fonts.googleapis.com/css2?family=Dosis:wght@500;600&family=Montserrat:wght@400;500&family=Yanone+Kaffeesatz:wght@400;500&display=swap">
<style>
  :root {
    --stage: #cfcccb;
    --paper: #ffffff;
    --paper-warm: #faf9f7;
    --ink: #4a4a4a;
    --ink-dark: #333333;
    --frame: #5c5c5c;
    --brand-blue: #3176b5;
    --brand-violet: #5b6db3;
    --sky: #0492cd;
    --sky-soft: #8fd0ef;
    --sky-pale: #cdeaf8;
    --badge: #4e73b8;
    --badge-box: #1f7cc4;
    --bloom-pink: #eea4c8;
    --perforation: #9a9a9a;
  }
  * { box-sizing: border-box; margin: 0; padding: 0; }
  html, body { width: 1200px; height: 1058px; overflow: hidden; }
  body {
    background: var(--stage);
    font-family: "Montserrat", sans-serif;
    color: var(--ink);
    position: relative;
  }

  .panel { position: absolute; background: var(--paper); overflow: hidden; }
  .panel--sachet { left: 70px; top: 250px; width: 437px; height: 740px; }
  .panel--front  { left: 545px; top: 150px; width: 380px; height: 860px; background: var(--paper-warm); }
  .panel--side   { left: 925px; top: 150px; width: 200px; height: 860px; background: var(--paper-warm); }

  .wash {
    position: absolute;
    left: 0; right: 0;
    background: linear-gradient(180deg, rgba(205,234,248,0) 0%, var(--sky-pale) 25%, var(--sky-soft) 70%, var(--sky) 100%);
  }
  .wash--top {
    top: 0; height: 160px;
    background: linear-gradient(180deg, var(--sky-pale) 0%, rgba(205,234,248,0.5) 55%, rgba(255,255,255,0) 100%);
  }
  .florals {
    position: absolute;
    left: 0; right: 0; bottom: 0;
    background: linear-gradient(180deg, var(--sky-soft) 0%, var(--bloom-pink) 100%);
  }

  .frame {
    position: absolute;
    border: 2px solid var(--frame);
    background: var(--paper);
  }
  .frame::after {
    content: "";
    position: absolute;
    inset: 12px;
    border: 1px solid var(--frame);
  }
  .panel--sachet .frame { left: 55px; top: 88px; width: 331px; height: 423px; }
  .panel--front .frame  { left: 40px; top: 228px; width: 310px; height: 430px; }

  .brand { position: absolute; left: 0; right: 0; text-align: center; z-index: 2; }
  .brand__mark {
    display: block;
    width: 56px; height: 56px;
    margin: 0 auto 20px;
    border-radius: 50%;
    background: var(--brand-violet);
  }
  .panel--front .brand__mark { background: var(--brand-blue); width: 50px; height: 50px; margin-bottom: 10px; }
  .brand__name {
    display: inline-block;
    font-weight: 500;
    font-size: 34px;
    letter-spacing: 0.5px;
    color: var(--brand-violet);
    line-height: 1.1;
  }
  .panel--front .brand__name { color: var(--brand-blue); font-size: 31px; }
  .brand__tagline { margin-top: 6px; font-size: 11px; font-weight: 500; color: var(--ink-dark); }
  .panel--sachet .brand { top: 52px; }
  .panel--front .brand  { top: 215px; }

  .product-name {
    position: absolute;
    left: 0; right: 0;
    text-align: center;
    font-family: "Dosis", sans-serif;
    font-weight: 600;
    color: var(--ink);
    z-index: 2;
  }
  .panel--sachet .product-name { top: 241px; font-size: 48px; line-height: 1.42; }
  .panel--front .product-name  { top: 380px; font-size: 44px; line-height: 1.43; }

  .claim {
    position: absolute;
    left: 0; right: 0;
    text-align: center;
    font-size: 14px;
    line-height: 1.3;
    color: var(--ink-dark);
    z-index: 2;
  }
  .panel--sachet .claim { top: 412px; }
  .panel--front .claim  { top: 533px; }

  .count-badge {
    position: absolute;
    width: 94px; height: 94px;
    border-radius: 50%;
    border: 3px solid var(--paper);
    background: var(--badge);
    color: var(--paper);
    text-align: center;
    z-index: 3;
  }
  .count-badge__num { display: block; font-family: "Dosis", sans-serif; font-weight: 600; font-size: 44px; line-height: 1; margin-top: 12px; }
  .count-badge__unit { display: block; font-size: 13px; letter-spacing: 0.5px; }
  .panel--sachet .count-badge { left: 29px; top: 460px; }
  .panel--front .count-badge  { left: 27px; top: 575px; background: var(--badge-box); width: 74px; height: 74px; }
  .panel--front .count-badge__num { font-size: 34px; margin-top: 8px; }
  .panel--front .count-badge__unit { font-size: 11px; }

  .tear-slot { position: absolute; left: 0; top: 0; width: 380px; height: 180px; z-index: 2; }
  .tear-slot__label {
    position: absolute;
    left: 160px; top: 106px;
    width: 44px; height: 38px;
    border-radius: 50% 50% 50% 50% / 45% 45% 55% 55%;
    background: var(--badge-box);
    color: var(--paper);
    font-family: "Yanone Kaffeesatz", sans-serif;
    font-size: 13px;
    line-height: 1;
    text-align: center;
    padding-top: 6px;
    z-index: 3;
  }

  .benefits {
    position: absolute;
    left: 20px; top: 285px;
    width: 175px;
    font-family: "Yanone Kaffeesatz", sans-serif;
    color: var(--ink-dark);
    z-index: 2;
  }
  .benefits__title { font-size: 16px; font-weight: 500; margin-bottom: 18px; }
  .benefits__list { list-style: none; font-size: 14px; line-height: 1.5; }
  .benefits__list li { position: relative; padding-left: 12px; }
  .benefits__list li::before {
    content: "";
    position: absolute;
    left: 0; top: 7px;
    width: 6px; height: 6px;
    border-radius: 50%;
    background: var(--ink-dark);
  }
</style>
</head>
<body>

  <section class="panel panel--sachet" aria-label="Sachet front">
    <div class="wash" style="top:340px;height:260px;"></div>
    <div class="florals" role="img" aria-label="Watercolour flowers and lemon balm leaves" style="height:200px;"></div>
    <div class="frame"></div>
    <div class="brand">
      <span class="brand__mark"></span>
      <span class="brand__name">VelvaDorm</span>
      <p class="brand__tagline">Clean modern for young women</p>
    </div>
    <h1 class="product-name">Collagen<br>Milk Powder</h1>
    <p class="claim">Maintain your healthy skin<br>while sleeping</p>
    <div class="count-badge"><span class="count-badge__num">5</span><span class="count-badge__unit">sachets</span></div>
  </section>

  <section class="panel panel--front" aria-label="Carton front">
    <div class="wash wash--top"></div>
    <div class="wash" style="top:480px;height:220px;"></div>
    <div class="florals" role="img" aria-label="Watercolour flowers and lemon balm leaves" style="height:200px;"></div>
    <svg class="tear-slot" viewBox="0 0 380 180" aria-hidden="true">
      <polyline points="0,70 182,147 380,0" fill="none" stroke="var(--perforation)" stroke-width="2.5" stroke-dasharray="3 4"/>
    </svg>
    <div class="tear-slot__label">tear<br>here</div>
    <div class="frame"></div>
    <div class="brand">
      <span class="brand__mark"></span>
      <span class="brand__name">VelvaDorm</span>
      <p class="brand__tagline">Clean modern for young women</p>
    </div>
    <h2 class="product-name">Collagen<br>Milk Powder</h2>
    <p class="claim">Maintain your healthy skin<br>while sleeping</p>
    <div class="count-badge"><span class="count-badge__num">5</span><span class="count-badge__unit">sachets</span></div>
  </section>

  <section class="panel panel--side" aria-label="Carton side">
    <div class="wash wash--top"></div>
    <div class="wash" style="top:470px;height:390px;"></div>
    <div class="florals" role="img" aria-label="Watercolour lemon balm leaves" style="height:180px;"></div>
    <div class="benefits">
      <p class="benefits__title">Benefits of Collagen Milk Powder :</p>
      <ul class="benefits__list">
        <li>Supporting hair, skin and nails</li>
        <li>For joint health</li>
        <li>To encourage skin elasticity and</li>
        <li>Reduce the signs of aging</li>
        <li>Improving digestion</li>
        <li>As a protein source</li>
      </ul>
    </div>
  </section>

</body>
</html>
```